Bramblewick Keystone

Looking for modern business cards.
Clean contemporary design.
Similar to this.
https://www.snapvorlo.net/imgview?src=https%3A%2F%2Fcdn.printquell.net%2Fprofessional_elegant_modern_black_plain_metal_business_card-a1b2c3d4e5f60718293a4b5c6d7e8f90_qwxyz_4tmpl_540.jpg&ref=https%3A%2F%2Fwww.printquell.net%2Fprofessional_elegant_modern_black_plain_metal_business_card-100200300400500600&id=7aB9cD3e-QR5TU&tid=Xyz_abc123defGH%3A&v=10abcDEFghiJKLmnoPQRstUVwxYZ0123456789abcd..x&w=540&h=540&bih=1360&biw=1061&q=modern%20business%20cards&ref2=0abcDEFghiJKLmnoPQRstUVwxYZ0123456789abcd&ia=mrc&ua=8

But I'd like the blue to look metallic.

```html
<!DOCTYPE html>
<html lang="en">
<head>
<meta charset="utf-8">
<title>Bramblewick Keystone — Business Cards</title>
<link rel="stylesheet" href="https://fonts.googleapis.com/css2?family=Arimo:ital,wght@0,400;0,700;1,700&display=swap">
<style>
  :root {
    --page: #eceff1;
    --card-white: #ffffff;
    --ink-navy: #1f3d57;
    --ink-black: #1a1a1a;
    --rule: #2b2b2b;
    --accent-teal: #1b8fae;
    --steel-deep: #0e6f94;
    --steel-mid: #2b8db2;
    --steel-light: #6fb6cf;
    --text-on-steel: #eef7fb;
  }
  * { box-sizing: border-box; margin: 0; padding: 0; }
  html, body {
    width: 1200px; height: 800px; overflow: hidden;
    background: var(--page);
    font-family: "Arimo", Arial, sans-serif;
  }
  .sheet {
    width: 1200px; height: 800px;
    display: flex; align-items: center; justify-content: center; gap: 48px;
  }
  .card {
    width: 525px; height: 300px;
    border-radius: 4px;
    box-shadow: 0 6px 18px rgba(0,0,0,.12);
    position: relative; overflow: hidden;
  }

  /* Front: contact side */
  .card--contact {
    background: var(--card-white);
    display: flex; align-items: center;
  }
  .identity {
    width: 48%;
    display: flex; flex-direction: column; align-items: center;
    text-align: center;
  }
  .identity__brand {
    display: flex; align-items: center; gap: 6px;
    font-size: 11px; font-weight: 700; color: var(--accent-teal);
    letter-spacing: .02em; margin-bottom: 14px; white-space: nowrap;
  }
  .identity__dot {
    width: 9px; height: 9px; border-radius: 50%; background: var(--accent-teal);
  }
  .identity__name {
    font-size: 22px; font-weight: 700; color: var(--ink-navy);
    letter-spacing: .04em; line-height: 1; white-space: nowrap;
  }
  .identity__role {
    font-size: 15px; color: var(--ink-black); margin-top: 4px;
  }
  .divider {
    width: 1.5px; height: 128px; background: var(--rule); flex: none;
  }
  .contact {
    padding-left: 30px;
    list-style: none;
    font-size: 13.5px; line-height: 1.55; color: var(--ink-black);
    white-space: nowrap;
  }

  /* Back: brushed metallic brand side */
  .card--brand {
    background:
      repeating-linear-gradient(0deg, rgba(255,255,255,.05) 0 1px, rgba(0,0,0,.04) 1px 2px, transparent 2px 4px),
      linear-gradient(100deg, rgba(255,255,255,0) 20%, rgba(255,255,255,.28) 48%, rgba(255,255,255,0) 70%),
      linear-gradient(180deg, var(--steel-deep) 0%, var(--steel-mid) 55%, var(--steel-light) 100%);
    display: flex; align-items: center; justify-content: center;
  }
  .brand {
    display: flex; flex-direction: column; align-items: flex-start;
  }
  .brand__lockup {
    display: flex; align-items: center; gap: 12px;
    color: var(--text-on-steel);
    font-size: 38px; font-weight: 400; letter-spacing: -.01em;
    white-space: nowrap;
  }
  .brand__dot {
    width: 22px; height: 22px; border-radius: 50%; background: var(--text-on-steel);
  }
  .brand__tagline {
    margin-top: 8px; margin-left: 34px;
    font-size: 10px; font-weight: 700; font-style: italic;
    color: var(--text-on-steel); letter-spacing: .03em;
  }
</style>
</head>
<body>
  <main class="sheet">
    <section class="card card--contact" aria-label="Business card front">
      <div class="identity">
        <div class="identity__brand"><span class="identity__dot"></span>Bramblewick Keystone</div>
        <h1 class="identity__name">MARLOW FENWICK</h1>
        <p class="identity__role">Director</p>
      </div>
      <div class="divider"></div>
      <ul class="contact">
        <li>bramblewickkeystone.net</li>
        <li>555 014 2738</li>
        <li>hello@bramblewickkeystone.net</li>
      </ul>
    </section>

    <section class="card card--brand" aria-label="Business card back">
      <div class="brand">
        <div class="brand__lockup"><span class="brand__dot"></span>Bramblewick Keystone</div>
        <p class="brand__tagline">“Steady Counsel for Ventures on the Rise”</p>
      </div>
    </section>
  </main>
</body>
</html>
```